Personal Finance e-commerce website needs a simple budget design

Hello! I am starting to sell downloadable and printable budget planners, as shown in the attached file, for people to plan ahead on their personal finances. <br/><br/>I want to see a one-page design with similar columns (for example, "Expenses, Budget, and Actual"). I would also like to see the basic formula ("Net Income = Gross income - Total Expenses") somewhere on the design. Finally, I want the design to remain mostly minimalistic and simple for the average person to plan their personal monthly budgets.<br/><br/>However, other than that, the overall design, layout, and colors will be at the graphic designer's choice. If you have any questions for me, please let me know. Thank you for your time!

Industry/Entity Type

Financial Planning

Colors

Designer to choose colors to be used in the design.

Requirements
Must have
• I want to see a one-page design with similar columns (for example, "Expenses, Budget, and Actual").
• I want the design to remain mostly minimalistic and simple for the average person to plan their personal monthly budgets.
Nice to have
• I would also like to see the basic formula ("Net Income = Gross income - Total Expenses") somewhere on the design.

```html
<!DOCTYPE html>
<html lang="en">
<head>
<meta charset="UTF-8">
<title>Basic Monthly Budget</title>
<link href="https://fonts.googleapis.com/css2?family=Saira+Stencil+One&family=Arimo:wght@400;700&display=swap" rel="stylesheet">
<style>
  :root {
    --backdrop: #d1d1d3;
    --paper: #ffffff;
    --ink: #111111;
    --hint: #b5b5b5;
    --expense-red: #ab1a27;
    --budget-green: #8cc63f;
    --actual-purple: #662d91;
  }
  * { margin: 0; padding: 0; box-sizing: border-box; }
  html, body {
    width: 960px; height: 1200px; overflow: hidden;
    background: var(--backdrop);
    font-family: "Arimo", Arial, sans-serif;
  }
  .sheet {
    position: absolute; left: 90px; top: 50px;
    width: 780px; height: 1100px;
    background: var(--paper);
  }
  .title {
    position: absolute; left: 0; right: 0; top: 40px;
    text-align: center;
    font-family: "Saira Stencil One", "Stardos Stencil", sans-serif;
    font-size: 70px; line-height: 1; color: var(--ink);
    letter-spacing: 1px;
  }
  .period {
    position: absolute; top: 122px; left: 394px;
    display: flex; align-items: baseline;
    font-size: 15px; color: var(--ink);
  }
  .period .blank {
    display: inline-block; width: 133px;
    border-bottom: 1.5px solid var(--ink);
    margin: 0 7px 0 5px;
  }
  .col-head {
    position: absolute; top: 161px; height: 48px;
    display: flex; align-items: center; justify-content: center;
    color: #fff; font-weight: 700; font-size: 31px; letter-spacing: 0.5px;
  }
  .expenses { left: 30px; width: 327px; background: var(--expense-red); }
  .budget   { left: 370px; width: 182px; background: var(--budget-green); }
  .actual   { left: 568px; width: 182px; background: var(--actual-purple); }
  .col-hint {
    position: absolute; top: 226px;
    text-align: center; color: var(--hint);
    font-size: 20px; line-height: 25px;
  }
  .col-hint.expenses-hint { left: 30px; width: 327px; top: 238px; }
  .col-hint.budget-hint { left: 370px; width: 182px; }
  .col-hint.actual-hint { left: 568px; width: 182px; }
  .rows {
    position: absolute; top: 287px; left: 30px;
    display: grid;
    grid-template-columns: 327px 182px 182px;
    column-gap: 13px;
    grid-auto-rows: 48px;
    row-gap: 10.4px;
  }
  .rows .cell { border: 1.6px solid var(--ink); background: var(--paper); }
  .rows .cell:nth-child(3n+3) { margin-left: 3px; width: 182px; }
  .formula-box {
    position: absolute; top: 943px; height: 48px; width: 182px;
    display: flex; align-items: center; justify-content: center;
    color: #fff; font-weight: 700; font-size: 21px;
  }
  .net   { left: 30px; background: var(--expense-red); }
  .gross { left: 299px; background: var(--budget-green); }
  .total { left: 568px; background: var(--actual-purple); }
  .operator { position: absolute; }
  .op-equals { left: 239px; top: 961px; }
  .op-minus  { left: 512px; top: 969px; }
  .formula-hint {
    position: absolute; top: 1012px; width: 182px;
    text-align: center; color: var(--hint);
    font-size: 20px; line-height: 25px;
  }
  .net-hint { left: 37px; }
  .gross-hint { left: 299px; }
  .total-hint { left: 568px; }
</style>
</head>
<body>
  <main class="sheet">
    <h1 class="title">Basic Monthly Budget</h1>
    <div class="period">Month<span class="blank"></span>Year<span class="blank"></span></div>

    <div class="col-head expenses">EXPENSES</div>
    <div class="col-head budget">BUDGET</div>
    <div class="col-head actual">ACTUAL</div>

    <p class="col-hint expenses-hint">Custom category</p>
    <p class="col-hint budget-hint">What you plan to<br>spend</p>
    <p class="col-hint actual-hint">What you actually<br>spent</p>

    <div class="rows">
      <div class="cell"></div><div class="cell"></div><div class="cell"></div>
      <div class="cell"></div><div class="cell"></div><div class="cell"></div>
      <div class="cell"></div><div class="cell"></div><div class="cell"></div>
      <div class="cell"></div><div class="cell"></div><div class="cell"></div>
      <div class="cell"></div><div class="cell"></div><div class="cell"></div>
      <div class="cell"></div><div class="cell"></div><div class="cell"></div>
      <div class="cell"></div><div class="cell"></div><div class="cell"></div>
      <div class="cell"></div><div class="cell"></div><div class="cell"></div>
      <div class="cell"></div><div class="cell"></div><div class="cell"></div>
      <div class="cell"></div><div class="cell"></div><div class="cell"></div>
      <div class="cell"></div><div class="cell"></div><div class="cell"></div>
    </div>

    <div class="formula-box net">Net Income</div>
    <svg class="operator op-equals" width="28" height="18" viewBox="0 0 28 18" aria-label="equals">
      <rect x="0" y="0" width="28" height="6" fill="var(--expense-red)"/>
      <rect x="0" y="12" width="28" height="6" fill="var(--expense-red)"/>
    </svg>
    <div class="formula-box gross">Gross income</div>
    <svg class="operator op-minus" width="18" height="6" viewBox="0 0 18 6" aria-label="minus">
      <rect x="0" y="0" width="18" height="6" fill="var(--expense-red)"/>
    </svg>
    <div class="formula-box total">Total Expenses</div>

    <p class="formula-hint net-hint">How much money<br>you kept</p>
    <p class="formula-hint gross-hint">How much money<br>you earned</p>
    <p class="formula-hint total-hint">Actual Expenses</p>
  </main>
</body>
</html>
```